Orthodontic Liaison Guild Annual Conference 2016 Flyer

We need a two page attention grabbing flyer promoting our upcoming conference in Dallas, TX at the Brackenridge Inn on August 27th and 28th 2016. The flyer should give information about the conference and what you will learn by attending and to accept registration through an Ticketvale link. Our mission is to define, educate and support the role of the dental implant coordinator. Bringing together like-minded professionals to network, practice share and define our role in the delivery of comprehensive patient care. 2 day annual conference open to Surgical implant coordinators and their surgeons

Target Market(s)

Surgical Implant Treatment Coordinators, their surgeons, and surgical team members

Industry/Entity Type

Dental

Requirements
Must have
• The ability for me to make changes.
Nice to have
• professional, eye catching,

```html
<!DOCTYPE html>
<html lang="en">
<head>
<meta charset="utf-8">
<title>Orthodontic Liaison Guild Annual Conference 2016</title>
<link href="https://fonts.googleapis.com/css2?family=Open+Sans:wght@400;600;700;800&family=Oswald:wght@500;700&display=swap" rel="stylesheet">
<style>
:root{
  --navy:#0d2b5e;
  --blue:#1f6fc4;
  --sky:#3a93e0;
  --ice:#e9f2fb;
  --ink:#1b2433;
  --white:#ffffff;
}
*{box-sizing:border-box;margin:0;padding:0}
html,body{width:900px;height:1200px;overflow:hidden;background:var(--white)}
body{font-family:"Open Sans",Arial,sans-serif;color:var(--ink)}
.flyer{position:relative;width:900px;height:1200px;overflow:hidden;background:var(--white)}
.brand{position:absolute;left:50px;top:60px;display:flex;align-items:center;gap:16px}
.brand-dot{width:58px;height:58px;border-radius:50%;background:var(--blue)}
.brand-name{font-weight:700;font-size:60px;color:var(--navy);letter-spacing:4px;line-height:1}
.brand-full{position:absolute;left:50px;top:138px;font-size:20px;font-weight:600;color:var(--blue)}
.hero-photo{position:absolute;right:0;top:0;width:470px;height:330px;
  background:linear-gradient(135deg,#f1d6cf,#e8a9a0 55%,#c9786f)}
.band{position:absolute;left:0;top:0;width:900px;height:1200px}
.headline{position:absolute;left:50px;top:250px;color:var(--white);line-height:1.05}
.headline .year{font-family:"Oswald",sans-serif;font-weight:700;font-size:64px}
.headline .org{font-family:"Oswald",sans-serif;font-weight:500;font-size:26px;letter-spacing:.5px;text-transform:uppercase}
.headline .event{font-family:"Oswald",sans-serif;font-weight:700;font-size:44px;text-transform:uppercase}
.headline .dates{font-weight:800;font-size:28px;margin-top:8px}
.headline .venue{font-weight:800;font-size:28px}
.highlights{position:absolute;left:0;top:520px;width:420px;height:360px;background:var(--navy);padding:28px 30px 0 40px;color:var(--white);list-style:none}
.highlights li{position:relative;padding-left:22px;font-size:15px;font-weight:600;line-height:1.35;margin-bottom:12px}
.highlights li::before{content:"";position:absolute;left:0;top:6px;width:9px;height:9px;background:var(--sky)}
.pricing{position:absolute;left:420px;top:520px;width:480px;height:360px;background:var(--blue);padding:40px 36px;color:var(--white)}
.pricing p{font-size:29px;font-weight:600;line-height:1.22}
.pricing .gap{margin-top:18px}
.speakers{position:absolute;left:0;top:880px;width:900px;height:220px;padding:26px 50px;background:var(--ice)}
.speakers h2{display:inline-block;background:var(--blue);color:var(--white);font-size:22px;font-weight:700;padding:6px 22px;margin-bottom:14px}
.speakers p{font-size:15px;line-height:1.5;color:var(--ink)}
.speakers .note{font-weight:700;margin-top:8px}
.footer{position:absolute;left:0;top:1100px;width:900px;height:100px;background:var(--navy);color:var(--white);padding:26px 50px;font-size:16px;font-weight:600;line-height:1.45}
</style>
</head>
<body>
<main class="flyer">
  <div class="hero-photo" role="img" aria-label="Close-up photo of a bright smile with white teeth"></div>

  <svg class="band" viewBox="0 0 900 1200" aria-hidden="true">
    <polygon points="0,250 900,180 900,520 0,520" fill="#1f6fc4"/>
    <polygon points="0,250 900,180 900,200 0,270" fill="#3a93e0"/>
  </svg>

  <div class="brand">
    <span class="brand-dot"></span>
    <span class="brand-name">OLG</span>
  </div>
  <div class="brand-full">Orthodontic Liaison Guild</div>

  <div class="headline">
    <div class="year">2016</div>
    <div class="org">Orthodontic Liaison Guild Association</div>
    <div class="event">OLG Conference</div>
    <div class="dates">Saturday 8/27 and Sunday 8/28</div>
    <div class="venue">at The Brackenridge Inn Dallas, TX</div>
  </div>

  <ul class="highlights">
    <li>Conference open to Surgical Implant Treatment Coordinators and their surgeons</li>
    <li>2-day Annual Orthodontic Liaison Guild conference</li>
    <li>Great speakers and topic lineup</li>
    <li>Breakout sessions including internet marketing, financial, communication, and patient care</li>
    <li>Additional credentials for early registered and OTC only</li>
    <li>Q&amp;A and practice sharing from a Surgeon/OTC panel with team and forms practice</li>
  </ul>

  <section class="pricing">
    <p>Cost by June 30th $699</p>
    <p>after June 30th $769</p>
    <p class="gap">OLG member cost $100 off conference registration</p>
    <p class="gap">Multiple team member discount $75 off conference registration</p>
  </section>

  <section class="speakers">
    <h2>Speakers</h2>
    <p>Dr. Elias Varnholt DDS, MSD, Prosthodontist "Healthy Implants from Start to Finish". Marisol Trent, Body Language Expert and contributor "The Body Language of Effective Communication". Dr. Owen Castellane DDS, Professor of Surgery "The Effective Role of the Implant Coordinator". Priya Dunmore, Professional Speaker and Coach, "Team Building, Communication, and Case Acceptance".</p>
    <p class="note">Breakfast and Lunch included</p>
  </section>

  <footer class="footer">
    Book your hotel reservation at The Brackenridge Inn $169/night room block through August 4, 2016
    https://ticketvale.example/olg-2016
  </footer>
</main>
</body>
</html>
```